business cards for a real estate investment company
Corva Homebuyers
Hi,
Can you check the draft #130, #131, #132, #133, #134, #135 and #136.
Thanks
Hello vostrapixel. I was really hoping to see some updated designs. I like what you've done so far and was hoping to give you the money. The drafts i mentioned above are almost perfect except< again, I'd love to see the term "Homebuilders" along with the logo so it's more obvious what services we provide. Thank you and I hope to see some more great work
TK/RPF/NW Team
Hello. One more note! I really like #45 as well. Same notes and changes apply. Thanks again
Hi vostrapixel. I really love design number 63. One thing I would like you to incorporate is "Homebuyers LLC". Maybe place the phrase somewhere around the corva logo. I'll trust your sensibility. Looking back, I really like number 47 as well, but with 63's backside, and again including "Homebuyers LLC". Thank you so much and I look forward to your modifications.

```html
<!DOCTYPE html>
<html lang="en">
<head>
<meta charset="utf-8">
<title>Corva Homebuyers – Business Card</title>
<link href="https://fonts.googleapis.com/css2?family=Raleway:wght@400;500;600;800&display=swap" rel="stylesheet">
<style>
  :root {
    --page-bg: #e9e6e1;
    --card-white: #ffffff;
    --brand-blue: #1b5cbf;
    --brand-blue-deep: #0c3d8e;
    --brand-green: #5aab34;
    --brand-green-light: #8fd15a;
    --text-light: #ffffff;
  }
  html, body {
    margin: 0;
    width: 1200px;
    height: 914px;
    overflow: hidden;
    background: var(--page-bg);
    font-family: "Raleway", sans-serif;
  }
  .card {
    position: absolute;
    left: 100px;
    top: 171px;
    width: 1000px;
    height: 571px;
    background: var(--card-white);
    box-shadow: 0 12px 30px rgba(0,0,0,0.18);
    overflow: hidden;
  }
  .card-shapes {
    position: absolute;
    inset: 0;
  }
  .person {
    position: absolute;
    right: 490px;
    top: 54px;
    text-align: right;
    color: var(--text-light);
    text-transform: uppercase;
    letter-spacing: 2px;
  }
  .person-name {
    font-size: 24px;
    font-weight: 500;
    margin: 0;
    white-space: nowrap;
  }
  .person-title {
    font-size: 15px;
    font-weight: 400;
    margin: 6px 0 0;
  }
  .contact-list {
    position: absolute;
    left: 70px;
    top: 300px;
    margin: 0;
    padding: 0;
    list-style: none;
    color: var(--text-light);
    font-size: 17px;
    letter-spacing: 1.5px;
    text-transform: uppercase;
  }
  .contact-list li {
    display: flex;
    align-items: center;
    gap: 12px;
    height: 38px;
    white-space: nowrap;
  }
  .contact-icon {
    width: 22px;
    height: 22px;
    flex: none;
  }
  .brand {
    position: absolute;
    left: 650px;
    top: 235px;
    display: flex;
    flex-direction: column;
    align-items: flex-start;
  }
  .brand-row {
    display: flex;
    align-items: center;
    gap: 14px;
  }
  .brand-dot {
    width: 26px;
    height: 26px;
    border-radius: 50%;
    background: var(--brand-green);
  }
  .brand-name {
    font-size: 78px;
    font-weight: 800;
    color: var(--brand-blue);
    line-height: 1;
  }
  .brand-tagline {
    margin: 10px 0 0 40px;
    font-size: 20px;
    font-weight: 600;
    letter-spacing: 3px;
    text-transform: uppercase;
    color: var(--brand-green);
  }
</style>
</head>
<body>
  <div class="card">
    <svg class="card-shapes" width="1000" height="571" viewBox="0 0 1000 571" aria-hidden="true">
      <defs>
        <linearGradient id="blueFill" x1="0" y1="0" x2="1" y2="1">
          <stop offset="0" stop-color="#1b5cbf"/>
          <stop offset="1" stop-color="#0c3d8e"/>
        </linearGradient>
        <linearGradient id="greenFill" x1="0" y1="0" x2="0" y2="1">
          <stop offset="0" stop-color="#8fd15a"/>
          <stop offset="1" stop-color="#5aab34"/>
        </linearGradient>
      </defs>
      <path d="M0,0 H600 C560,60 520,140 540,240 C560,360 520,470 470,571 H0 Z" fill="url(#blueFill)"/>
      <path d="M640,70 C575,150 560,210 575,280 C595,380 560,460 500,571 H470 C520,470 560,360 540,240 C530,170 570,110 640,70 Z" fill="url(#greenFill)"/>
    </svg>

    <div class="person">
      <p class="person-name">Dana Whitcombe</p>
      <p class="person-title">Managing Partner</p>
    </div>

    <ul class="contact-list">
      <li>
        <svg class="contact-icon" viewBox="0 0 24 24"><circle cx="12" cy="12" r="12" fill="#fff"/><path d="M8.5 6.5l2 2-1.2 1.6c.8 1.6 2 2.8 3.6 3.6l1.6-1.2 2 2-1.4 1.8c-4.2-.6-7.6-4-8.2-8.2z" fill="#1b5cbf"/></svg>
        <span>555-301-0147</span>
      </li>
      <li>
        <svg class="contact-icon" viewBox="0 0 24 24"><circle cx="12" cy="12" r="12" fill="#fff"/><rect x="6" y="8" width="12" height="8" rx="1" fill="#1b5cbf"/><path d="M6.5 8.5l5.5 4 5.5-4" stroke="#fff" stroke-width="1.2" fill="none"/></svg>
        <span>corvahomebuyers@corvamail.com</span>
      </li>
      <li>
        <svg class="contact-icon" viewBox="0 0 24 24"><circle cx="12" cy="12" r="12" fill="#fff"/><circle cx="12" cy="12" r="6" stroke="#1b5cbf" stroke-width="1.4" fill="none"/><path d="M6 12h12M12 6c-2.5 3-2.5 9 0 12M12 6c2.5 3 2.5 9 0 12" stroke="#1b5cbf" stroke-width="1.2" fill="none"/></svg>
        <span>www.corvahomebuyers.com</span>
      </li>
    </ul>

    <div class="brand">
      <div class="brand-row">
        <span class="brand-dot"></span>
        <span class="brand-name">Corva</span>
      </div>
      <p class="brand-tagline">Homebuyers LLC</p>
    </div>
  </div>
</body>
</html>
```